Website Design For Physical Therapy/Sports Massage Clinic

Hi! I am looking for a sleek, fun and functional new wordpress website for my physical therapy/sports massage clinic. My current site is www.velmoracarestudio.com. As you can see it's very basic and well... boring. :) In addition to a fun new look, I would also love this to be mobile friendly.

In terms of add on services/widgets I would like to use Brindle Booking + Quill Consent so that people can schedule and fill out paperwork remotely. Both seem like easy add ons to any site, but just in case here are the sites for both to ensure compatibility with the new design.

https://secure.brindlebooking.com/
https://www.quillconsent.com/

Thanks for reading and I'm excited to get started. I would love to see designs that are modern, athlete minded and fun as those are my clients. Attached you will find two logos (one white and one blue).

Target Market(s)

Athletes and weekend warriors

Industry/Entity Type

Physical Therapy

Number of Pages Required

1 page

Font styles to use
Sans Serif

Requirements
Must have
• 1) A fun home page that is modern and easy to navigate and 2) a website that is compatible with Brindle booking + quill consent so that my patients can schedule and fill out their paperwork without me.

```html
<!DOCTYPE html>
<html lang="en">
<head>
<meta charset="utf-8">
<title>Velmora Care Studio</title>
<link href="https://fonts.googleapis.com/css2?family=Lato:wght@400;700;900&family=Questrial&display=swap" rel="stylesheet">
<style>
:root{
  --blue:#0e4c8d;
  --blue-dark:#0a3b72;
  --blue-btn:#123f87;
  --orange:#f7841f;
  --ink:#222;
  --text:#444;
  --muted:#777;
  --line:#cfcfcf;
  --footer:#333333;
  --footer-dark:#1e1e1e;
  --white:#fff;
}
*{margin:0;padding:0;box-sizing:border-box}
html,body{width:1200px;height:2862px;overflow:hidden;background:var(--white)}
body{font-family:"Lato",sans-serif;color:var(--text);position:relative}
.abs{position:absolute}
.heading{font-family:"Questrial",sans-serif;color:var(--ink);font-weight:400}

/* header */
.site-header{position:absolute;left:0;top:0;width:1200px;height:113px;background:linear-gradient(180deg,#125296,#0c4482)}
.brand{position:absolute;left:99px;top:38px;display:flex;align-items:center;gap:12px;color:var(--white);font-family:"Lato",sans-serif;font-weight:900;font-size:22px;letter-spacing:1px}
.brand-mark{width:30px;height:30px;background:var(--orange)}
.call{position:absolute;left:727px;top:22px;color:var(--white);font-size:15px;letter-spacing:.5px}
.phone-pill{position:absolute;left:944px;top:16px;width:157px;height:34px;border:1.5px solid var(--white);border-radius:17px;display:flex;align-items:center;gap:8px;padding-left:4px;color:var(--white);font-size:16px;font-weight:700}
.phone-pill .dot{width:26px;height:26px;border-radius:50%;background:var(--white);display:flex;align-items:center;justify-content:center}
.main-nav{position:absolute;top:76px;left:0;width:1200px}
.main-nav a{position:absolute;color:var(--white);text-decoration:none;font-size:15px;letter-spacing:.4px}
.main-nav a.active{font-weight:700;border-bottom:2px solid var(--white);padding-bottom:6px}

/* hero */
.hero{position:absolute;left:0;top:113px;width:1200px;height:469px;background:radial-gradient(ellipse at 70% 40%,#4a4a4a 0%,#262626 45%,#141414 100%)}
.hero-title{position:absolute;left:99px;top:250px;font-family:"Questrial",sans-serif;color:var(--white);font-size:31px;line-height:42px}
.btn-outline{position:absolute;left:99px;top:391px;width:239px;height:51px;border:1.5px solid var(--white);color:var(--white);font-weight:700;font-size:19px;display:flex;align-items:center;justify-content:center}
.arrow{position:absolute;top:198px}

/* welcome */
.welcome-title{left:99px;top:624px;font-size:33px}
.rule{position:absolute;height:1px;background:var(--line)}
.lead{left:99px;top:696px;width:650px;font-weight:700;font-size:16px;line-height:25px;color:var(--ink)}
.body-copy{left:99px;top:755px;width:650px;font-size:14px;line-height:23.6px;color:var(--text)}
.btn-solid{position:absolute;background:var(--blue-btn);color:var(--white);font-weight:700;display:flex;align-items:center;justify-content:center}
.inquiry{position:absolute;left:778px;top:652px;width:323px;height:294px;border:1.5px solid #ddd}
.inquiry-title{position:absolute;left:22px;top:-17px;background:var(--white);padding:0 10px;font-size:28px}
.field{position:absolute;left:17px;width:289px;height:34px;border:1.5px solid #ddd;font-size:12px;color:#999;padding:9px 10px}
.schedule-link{position:absolute;left:146px;top:253px;font-size:12px;font-weight:700;color:#333}

/* services */
.services{position:absolute;left:0;top:998px;width:1200px;height:437px;background:linear-gradient(180deg,#2a3540 0%,#1f3a52 50%,#243847 100%)}
.section-title{position:absolute;width:1200px;text-align:center;font-family:"Questrial",sans-serif;font-size:31px}
.service-card{position:absolute;top:151px;width:304px;height:244px}
.service-photo{position:absolute;left:0;top:0;width:304px;height:168px}
.service-label{position:absolute;left:0;top:168px;width:304px;height:76px;background:rgba(105,105,105,.92);color:var(--white);font-family:"Questrial",sans-serif;font-size:21px;line-height:25px;display:flex;align-items:center;justify-content:center;padding-right:70px;text-align:center}
.plus{position:absolute;right:0;top:168px;width:73px;height:76px;background:var(--orange);clip-path:polygon(38% 0,100% 0,100% 100%,0 100%);display:flex;align-items:center;justify-content:flex-end;padding-right:20px;color:var(--white);font-size:34px;font-weight:700}

/* why */
.video{position:absolute;left:99px;top:1555px;width:506px;height:319px;background:radial-gradient(ellipse at 55% 40%,#6d7f86,#3e4a4e 70%,#2a3032)}
.video-bar{position:absolute;left:0;bottom:0;width:100%;height:34px;background:rgba(0,0,0,.85)}
.feature-title{position:absolute;left:717px;font-weight:700;font-size:18px;color:var(--ink)}
.feature-text{position:absolute;left:717px;width:385px;font-size:13px;line-height:22px;color:var(--text)}

/* blog */
.blog{position:absolute;left:0;top:1927px;width:1200px;height:330px;background:var(--blue)}
.post-photo{position:absolute;top:109px;width:168px;height:177px}
.post-title{position:absolute;top:112px;color:var(--white);font-weight:700;font-size:14.5px;width:310px}
.post-date{position:absolute;top:138px;color:#dfe8f3;font-size:10.5px}
.post-text{position:absolute;top:160px;color:var(--white);font-size:12.5px;line-height:20px;width:310px}
.post-more{position:absolute;top:255px;color:var(--white);font-size:12.5px;text-decoration:underline}

/* newsletter */
.news-copy{position:absolute;left:100px;top:2366px;width:1000px;text-align:center;font-size:14.5px;line-height:23px;color:var(--ink)}
.email{position:absolute;left:298px;top:2433px;width:423px;height:42px;border:1.5px solid #bbb;font-size:12px;color:#999;padding:13px 14px}

/* footer */
.footer{position:absolute;left:0;top:2528px;width:1200px;height:281px;background:var(--footer)}
.foot-head{position:absolute;top:40px;color:var(--orange);font-weight:700;font-size:17px}
.foot-list{position:absolute;left:99px;top:83px;list-style:none}
.foot-list li{color:#ddd;font-size:12.5px;height:24.4px;padding-left:16px;position:relative}
.foot-list li::before{content:"›";position:absolute;left:0;color:var(--orange)}
.contact-line{position:absolute;left:267px;color:#ddd;font-size:12.5px;line-height:21px;display:flex;gap:10px}
.map{position:absolute;left:513px;top:44px;width:323px;height:195px;background:linear-gradient(135deg,#e8e4da,#d9dde0 60%,#cfd8c8)}
.foot-brand{position:absolute;left:897px;top:100px;width:204px;text-align:center;color:#8a8a8a;font-weight:900;font-size:20px;letter-spacing:1px;display:flex;align-items:center;justify-content:center;gap:8px}
.foot-brand .sq{width:22px;height:22px;background:#8a8a8a}
.social{position:absolute;top:178px;width:34px;height:34px;border-radius:50%;border:1.5px solid #ccc}
.copyright{position:absolute;left:0;top:2809px;width:1200px;height:53px;background:var(--footer-dark);color:#ccc;font-size:12.5px;display:flex;align-items:center;justify-content:center}
</style>
</head>
<body>

<header class="site-header">
  <div class="brand"><span class="brand-mark"></span>VELMORA CARE STUDIO</div>
  <div class="call">PLEASE CALL TO SCHEDULE</div>
  <div class="phone-pill"><span class="dot"><svg width="14" height="14" viewBox="0 0 24 24"><path fill="#0e4c8d" d="M6.6 10.8a15 15 0 0 0 6.6 6.6l2.2-2.2a1 1 0 0 1 1-.25 11.4 11.4 0 0 0 3.6.6 1 1 0 0 1 1 1V20a1 1 0 0 1-1 1A17 17 0 0 1 3 4a1 1 0 0 1 1-1h3.5a1 1 0 0 1 1 1c0 1.25.2 2.45.6 3.6a1 1 0 0 1-.25 1z"/></svg></span>(512)555-0148</div>
  <nav class="main-nav">
    <a class="active" style="left:395px">HOME</a>
    <a style="left:484px">ABOUT</a>
    <a style="left:575px">SERVICES</a>
    <a style="left:688px">NEW PATIENTS</a>
    <a style="left:843px">PRICING</a>
    <a style="left:945px">BLOG</a>
    <a style="left:1027px">CONTACT</a>
  </nav>
</header>

<section class="hero" role="img" aria-label="Athlete chalking hands beside a loaded barbell in a dark gym">
  <svg class="arrow" style="left:32px" width="34" height="64" viewBox="0 0 34 64"><path d="M30 2 4 32l26 30" fill="none" stroke="#fff" stroke-width="2"/></svg>
  <svg class="arrow" style="left:1134px" width="34" height="64" viewBox="0 0 34 64"><path d="M4 2l26 30L4 62" fill="none" stroke="#fff" stroke-width="2"/></svg>
  <div class="hero-title" style="top:250px">Whatever Your Sport,<br>We Can Keep You Moving<br>Towards Your Fitness Goals..!</div>
  <div class="btn-outline">Schedule Appointment</div>
</section>

<section class="welcome">
  <h1 class="abs heading welcome-title">Welcome To VELMORA CARE STUDIO</h1>
  <div class="rule" style="left:99px;top:674px;width:649px"></div>
  <p class="abs lead">Lorem ipsum dolor sit amet, consectetur adipiscing elit. Sed vitae magna tellus. Aenean ante nunc, semper nec cursus non</p>
  <p class="abs body-copy">Lorem ipsum dolor sit amet, consectetur adipiscing elit. Sed vitae magna tellus. Aenean ante nunc, semper nec cursus non, rutrum ac eros. Vestibulum mattis justo ac dui bibendum consequat a ac ipsum. Praesent a arcu venenatis, auctor velit eu, suscipit libero. Quisque convallis, leo ac pharetra sagittis, ipsum arcu auctor urna, sit amet cursus risus augue in eros. Duis lacinia nisi vitae leo commodo, non finibus magna maximus. Sed posuere, neque eget bibendum pulvinar, ligula erat suscipit dolor, ut maximus arcu mi et tortor.</p>
  <div class="btn-solid" style="left:99px;top:914px;width:120px;height:32px;font-size:14px">READ MORE</div>

  <form class="inquiry">
    <div class="inquiry-title heading">Quick Inquiry</div>
    <div class="field" style="top:26px">Name</div>
    <div class="field" style="top:70px">Email Id</div>
    <div class="field" style="top:114px">Inquiry Type
      <svg style="position:absolute;right:10px;top:13px" width="10" height="6" viewBox="0 0 10 6"><path d="M0 0h10L5 6z" fill="#aaa"/></svg></div>
    <div class="field" style="top:158px;height:76px">Message</div>
    <div class="btn-solid" style="left:17px;top:243px;width:118px;height:32px;font-size:15px">SUBMIT</div>
    <div class="schedule-link" style="top:252px">Schedule Your Appointment</div>
  </form>
</section>

<section class="services">
  <h2 class="section-title" style="top:38px;color:#fff">Our Services</h2>
  <div class="rule" style="left:445px;top:83px;width:310px;background:rgba(255,255,255,.6)"></div>
  <p class="abs" style="left:0;top:108px;width:1200px;text-align:center;color:#fff;font-size:17px">Lorem ipsum dolor sit amet, consectetur adipiscing elit. Sed vitae magna tellus aenean ante nunc</p>

  <div class="service-card" style="left:99px">
    <div class="service-photo" role="img" aria-label="Therapist stretching a patient's leg" style="background:linear-gradient(135deg,#d9cfc6,#7aa4c4 60%,#3c6e9a)"></div>
    <div class="service-label">Physical Therapy</div>
    <div class="plus">+</div>
  </div>
  <div class="service-card" style="left:448px">
    <div class="service-photo" role="img" aria-label="Athlete's legs on a strength testing machine" style="background:linear-gradient(135deg,#e7e7e7,#9c9c9c 55%,#3a3a3a)"></div>
    <div class="service-label">Sport Specific<br>Analysis and Training</div>
    <div class="plus">+</div>
  </div>
  <div class="service-card" style="left:798px">
    <div class="service-photo" role="img" aria-label="Therapist checking a patient's blood pressure" style="background:linear-gradient(135deg,#f1ede8,#c9c2ba 50%,#5a6f8c)"></div>
    <div class="service-label">Wellness and<br>Maintenance Care</div>
    <div class="plus">+</div>
  </div>
</section>

<section class="why">
  <h2 class="section-title" style="top:1481px;color:var(--ink)">Why Choose Us?</h2>
  <div class="rule" style="left:460px;top:1527px;width:280px"></div>

  <div class="video" role="img" aria-label="Video still of an older man cycling outdoors">
    <svg style="position:absolute;left:233px;top:130px" width="42" height="42" viewBox="0 0 42 42"><circle cx="21" cy="21" r="20" fill="rgba(80,140,200,.85)"/><path d="M16 12l13 9-13 9z" fill="#fff"/></svg>
    <div class="video-bar">
      <svg style="position:absolute;left:10px;top:11px" width="34" height="12" viewBox="0 0 34 12"><path d="M0 0l9 6-9 6z" fill="#fff"/><rect x="18" y="0" width="3" height="12" fill="#fff"/><rect x="24" y="0" width="3" height="12" fill="#fff"/></svg>
      <div style="position:absolute;left:52px;top:15px;width:440px;height:4px;background:#666"></div>
      <div style="position:absolute;left:52px;top:15px;width:188px;height:4px;background:#c8102e"></div>
    </div>
  </div>

  <div style="position:absolute;left:677px;top:1575px;width:1px;height:280px;background:var(--line)"></div>
  <svg style="position:absolute;left:660px;top:1606px" width="34" height="30" viewBox="0 0 34 30"><rect x="0" y="0" width="34" height="30" fill="#fff"/><circle cx="12" cy="6" r="4" fill="#111"/><path d="M3 18h28v4H3zM8 12h16l3 5H6zM6 22v6M28 22v6" stroke="#111" stroke-width="2" fill="#111"/></svg>
  <div class="feature-title" style="top:1610px">Quality Hands On Time</div>
  <div class="feature-text" style="top:1637px">Velmora Care Studio has one goal: to get you back to what you love doing as fast as possible. <b>[...]</b></div>

  <svg style="position:absolute;left:662px;top:1692px" width="30" height="36" viewBox="0 0 30 36"><rect width="30" height="36" fill="#fff"/><path d="M8 22l12-18 6 4-12 18z" fill="#111"/><path d="M8 22l-3 10 8-6z" fill="#111"/></svg>
  <div class="feature-title" style="top:1701px">Effective Treatments</div>
  <div class="feature-text" style="top:1728px">Treatment techniques used at Velmora Care Studio include: Soft Tissue Release (STR), Kestrel Technique <b>[...]</b></div>

  <svg style="position:absolute;left:661px;top:1785px" width="32" height="34" viewBox="0 0 32 34"><rect width="32" height="34" fill="#fff"/><circle cx="20" cy="5" r="4" fill="#111"/><path d="M18 10l-6 8 6 4-3 10M18 10l5 8 6-2M12 18l-8 3" stroke="#111" stroke-width="3.5" fill="none" stroke-linecap="round"/></svg>
  <div class="feature-title" style="top:1793px">Education</div>
  <div class="feature-text" style="top:1820px">Battling an injury with a big race or competition looming? Velmora Care Studio can help. <b>[...]</b></div>
</section>

<section class="blog">
  <h2 class="section-title" style="top:40px;color:#fff">Latest Blog Posts</h2>
  <div class="rule" style="left:445px;top:86px;width:310px;background:rgba(255,255,255,.6)"></div>
  <svg class="arrow" style="left:36px;top:160px" width="24" height="72" viewBox="0 0 24 72"><path d="M22 2 3 36l19 34" fill="none" stroke="#fff" stroke-width="2"/></svg>
  <svg class="arrow" style="left:1140px;top:160px" width="24" height="72" viewBox="0 0 24 72"><path d="M2 2l19 34L2 70" fill="none" stroke="#fff" stroke-width="2"/></svg>

  <div class="post-photo" role="img" aria-label="Therapist treating a seated patient" style="left:99px;background:linear-gradient(135deg,#c9b8a6,#8a6e58 55%,#5b4536)"></div>
  <div class="post-title" style="left:284px">Sed ut perspiciatis unde omnis iste natus er</div>
  <div class="post-date" style="left:284px">31 March, 2016 &nbsp;|&nbsp; 03:26 pm</div>
  <div class="post-text" style="left:284px">Lorem ipsum dolor sit amet, consectetur adipiscing elit. Sed vitae magna tellus. Aenean ante nunc, semper nec cursus non, rutrum ac eros. Vestibulum mattis justo ac dui bibendum consequat a ac ipsum.</div>
  <div class="post-more" style="left:284px">Read More »</div>

  <div class="post-photo" role="img" aria-label="Two runners jogging on a grassy path" style="left:611px;background:linear-gradient(180deg,#b9c9a2,#6f8f4c 60%,#4c6a33)"></div>
  <div class="post-title" style="left:796px">Sed ut perspiciatis unde omnis iste natus er</div>
  <div class="post-date" style="left:796px">31 March, 2016 &nbsp;|&nbsp; 03:26 pm</div>
  <div class="post-text" style="left:796px">Lorem ipsum dolor sit amet, consectetur adipiscing elit. Sed vitae magna tellus. Aenean ante nunc, semper nec cursus non, rutrum ac eros. Vestibulum mattis justo ac dui bibendum consequat a ac ipsum.</div>
  <div class="post-more" style="left:796px">Read More »</div>
</section>

<section class="newsletter">
  <h2 class="section-title" style="top:2298px;color:var(--ink)">Newsletter Signup</h2>
  <div class="rule" style="left:460px;top:2344px;width:280px"></div>
  <p class="news-copy">Lorem ipsum dolor sit amet, consectetuer adipiscing elit, sed diam nonummy nibh euismod tincidunt ut laoreet dolore magna aliquam erat volutpat. Ut wisi enim ad minim veniam.</p>
  <div class="email">Enter your email address</div>
  <div class="btn-solid" style="left:735px;top:2433px;width:167px;height:42px;font-size:15px">SUBSCRIBE</div>
</section>

<footer class="footer">
  <div class="foot-head" style="left:99px">Quick Links</div>
  <div class="rule" style="left:99px;top:66px;width:111px;background:#666"></div>
  <ul class="foot-list">
    <li>Home</li><li>About</li><li>Services</li><li>New Patients</li><li>Pricing</li><li>Blog</li><li>Contact</li>
  </ul>

  <div class="foot-head" style="left:267px">Contact Details</div>
  <div class="rule" style="left:267px;top:66px;width:188px;background:#666"></div>
  <div class="contact-line" style="top:80px">
    <svg width="12" height="16" viewBox="0 0 12 16"><path d="M6 0a6 6 0 0 1 6 6c0 4-6 10-6 10S0 10 0 6a6 6 0 0 1 6-6z" fill="#f7841f"/><circle cx="6" cy="6" r="2" fill="#333"/></svg>
    <div><b style="color:#fff">Velmora Care Studio</b><br>2710 Harlow Ridge Rd, Ste 310<br>Dunmore, TX 78610</div>
  </div>
  <div class="contact-line" style="top:159px">
    <svg width="14" height="14" viewBox="0 0 24 24"><path fill="#f7841f" d="M6.6 10.8a15 15 0 0 0 6.6 6.6l2.2-2.2a1 1 0 0 1 1-.25 11.4 11.4 0 0 0 3.6.6 1 1 0 0 1 1 1V20a1 1 0 0 1-1 1A17 17 0 0 1 3 4a1 1 0 0 1 1-1h3.5a1 1 0 0 1 1 1c0 1.25.2 2.45.6 3.6a1 1 0 0 1-.25 1z"/></svg>
    <div>603-555-0192</div>
  </div>
  <div class="contact-line" style="top:190px">
    <svg width="14" height="14" viewBox="0 0 14 14"><rect x="1" y="4" width="12" height="8" fill="#f7841f"/><rect x="3" y="1" width="8" height="4" fill="none" stroke="#f7841f" stroke-width="1.5"/></svg>
    <div>844-555-0137</div>
  </div>
  <div class="contact-line" style="top:218px">
    <svg width="14" height="12" viewBox="0 0 14 12"><rect x="0" y="1" width="14" height="10" fill="#f7841f"/><path d="M0 1l7 6 7-6" fill="none" stroke="#333" stroke-width="1.2"/></svg>
    <div>info@velmoracarestudio.com</div>
  </div>

  <div class="map" role="img" aria-label="Street map showing the clinic location"></div>

  <div class="foot-brand"><span class="sq"></span>VELMORA</div>
  <div class="social" style="left:916px"></div>
  <div class="social" style="left:958px;border-color:var(--orange)"></div>
  <div class="social" style="left:1000px"></div>
  <div class="social" style="left:1044px"></div>
</footer>

<div class="copyright">Copyright © 2016 Velmora Care Studio. All Rights Reserved.</div>

</body>
</html>
```